Brightfold Systems, a software development company, needs a website

We need a website to promote our software development company. The company is brand new and we want to market ourselves. We develop all kinds of software from web applications, to desktop applications, to mobile applications. Small company, not a lot of history, just need something flashy.

```html
<!DOCTYPE html>
<html lang="en">
<head>
<meta charset="utf-8">
<title>Brightfold Systems</title>
<link href="https://fonts.googleapis.com/css2?family=Jost:wght@400;500;600&display=swap" rel="stylesheet">
<style>
:root{
  --blue:#2f8fd8;
  --blue-deep:#1f6fbf;
  --ink:#2b2b2b;
  --muted:#6b6f75;
  --line:#cfe0ef;
  --pale:#eaf3fa;
  --white:#fff;
}
*{box-sizing:border-box;margin:0;padding:0}
html,body{width:1200px;height:4225px;overflow:hidden}
body{font-family:'Jost',sans-serif;color:var(--ink);background:var(--white);position:relative}
.abs{position:absolute}
.btn{position:absolute;display:flex;align-items:center;justify-content:center;border-radius:30px;font-size:13px;font-weight:600;color:var(--white);background:linear-gradient(90deg,#35a3e0,var(--blue-deep))}
.btn.ghost{background:var(--white);color:var(--blue-deep)}
/* header */
.header{top:0;left:0;width:1200px;height:95px;background:var(--white)}
.brand{left:80px;top:24px;display:flex;align-items:center;gap:10px}
.brand-mark{width:30px;height:30px;background:var(--blue)}
.brand-name{font-size:24px;font-weight:600;color:var(--blue);line-height:1}
.nav{top:38px;font-size:13px;color:#444}
.nav.active{color:var(--blue)}
/* hero */
.hero{top:95px;left:0;width:1200px;height:544px;background:linear-gradient(100deg,#7e8a92 0%,#b9b7b1 45%,#d9d2c6 70%,#a7aeb4 100%)}
.hero h1{position:absolute;left:162px;top:160px;width:520px;font-size:39px;font-weight:400;line-height:46px;color:var(--white)}
.dot{position:absolute;left:1108px;width:11px;height:11px;border:1.5px solid var(--white);border-radius:50%}
.dot.on{background:var(--white)}
/* feature cards */
.card{position:absolute;width:270px;text-align:center}
.card.boxed{border:1.5px solid #8fc3ea;border-radius:3px;background:var(--white)}
.card h3{font-size:19px;font-weight:500;margin-bottom:10px}
.card p{font-size:13.5px;line-height:21px;color:var(--muted);padding:0 40px}
.more{position:absolute;left:0;width:100%;font-size:12px;color:var(--blue);text-align:center}
.icon{margin:0 auto 20px;display:block}
/* band */
.band{top:1070px;left:0;width:1200px;height:241px;background:linear-gradient(120deg,#2a78c4,#3d8fd6 50%,#2669b3)}
.band h2{position:absolute;top:48px;width:100%;text-align:center;font-size:36px;font-weight:400;color:var(--white)}
.band p{position:absolute;top:100px;width:100%;text-align:center;font-size:14px;color:var(--white)}
/* headings */
.sec-title{position:absolute;left:0;width:1200px;display:flex;justify-content:center;align-items:center;gap:24px;font-size:28px;font-weight:500}
.sec-title::before,.sec-title::after{content:"";width:80px;height:1px;background:#9cc8ea}
.about-title{left:80px;top:1484px;font-size:28px;font-weight:500;display:flex;align-items:center;gap:24px}
.about-title::after{content:"";width:78px;height:1px;background:#9cc8ea}
.about-lead{left:80px;top:1540px;width:450px;font-size:13.5px;line-height:21px;font-weight:500;color:#333}
.about-body{left:80px;top:1622px;width:440px;font-size:12px;line-height:19px;color:var(--muted)}
.blob-bg{left:720px;top:1393px;width:400px;height:490px;background:#e2f2fa;border-radius:48% 52% 45% 55%/40% 45% 55% 60%}
.blob-photo{left:629px;top:1440px;width:490px;height:448px;background:linear-gradient(135deg,#b7cbd6,#e7eef2 40%,#6f8da3 80%);border-radius:55% 45% 50% 50%/45% 55% 45% 55%}
.arrow{position:absolute;font-size:22px;color:#aab3bb}
/* work */
.work{top:2483px;left:0;width:1200px;height:579px;background:var(--pale)}
.shot{position:absolute;top:139px;height:359px}
.shot-caption{position:absolute;left:38px;bottom:28px;color:var(--white)}
.shot-caption b{display:block;font-size:18px;font-weight:600}
.shot-caption span{font-size:14px}
.pdot{position:absolute;top:533px;width:9px;height:9px;border:1px solid var(--blue);border-radius:50%}
/* testimonials */
.avatar{position:absolute;width:121px;height:123px;border-radius:50%;background:linear-gradient(160deg,#d8ecf6,#a9c0cf)}
.quote{position:absolute;width:250px;font-size:13px;line-height:22px;color:var(--muted)}
.person{position:absolute;font-size:13px;font-weight:600;color:var(--blue)}
.person small{display:block;font-size:11px;font-weight:400;color:#555}
.client-logo{position:absolute;top:3612px;width:160px;text-align:center;font-size:22px;font-weight:600;color:#a9adb2}
/* contact */
.contact-bg{top:3700px;left:0;width:1200px;height:460px;background:linear-gradient(180deg,#fff 0%,#f6f8fa 70%,#dfe6ec 100%)}
.field{position:absolute;border:1px solid #dfe3e7;border-radius:20px;background:var(--white);font-size:12px;color:#555;padding:0 22px;display:flex;align-items:center}
.field.area{align-items:flex-start;padding-top:12px;border-radius:14px}
.footer{top:4160px;left:0;width:1200px;height:65px;background:#2f3236;color:#c7cace;font-size:12px}
.social{position:absolute;top:19px;width:27px;height:27px;border-radius:50%;background:var(--blue)}
</style>
</head>
<body>

<header class="abs header">
  <div class="abs brand"><span class="brand-mark"></span><span class="brand-name">Brightfold Systems</span></div>
  <span class="abs nav active" style="left:379px">Home</span>
  <span class="abs nav" style="left:462px">About</span>
  <span class="abs nav" style="left:546px">Service</span>
  <span class="abs nav" style="left:639px">Work</span>
  <span class="abs nav" style="left:720px">Client</span>
  <span class="abs nav" style="left:801px">Reviews</span>
  <span class="abs nav" style="left:885px;font-size:12px">
    <svg width="9" height="12" viewBox="0 0 9 12" style="vertical-align:-1px"><rect x="1" y="0.5" width="7" height="11" rx="1.5" fill="none" stroke="#2f8fd8"/></svg>
    555.014.2290</span>
  <span class="btn" style="left:1008px;top:28px;width:112px;height:39px">Contact Us</span>
</header>

<section class="abs hero" role="img" aria-label="Photo of a smiling woman in glasses working at a laptop">
  <h1>We delivering great web applications and developing new products</h1>
  <span class="btn" style="left:159px;top:339px;width:177px;height:38px">Contact Us Today!</span>
  <span class="dot" style="top:231px"></span>
  <span class="dot on" style="top:255px"></span>
  <span class="dot" style="top:279px"></span>
  <span class="dot" style="top:303px"></span>
</section>

<section>
  <div class="card" style="left:160px;top:703px;height:303px">
    <svg class="icon" width="50" height="50" viewBox="0 0 50 50" style="margin-top:55px" fill="none" stroke="#2f8fd8" stroke-width="1.5"><rect x="16" y="6" width="26" height="34" rx="2"/><path d="M22 14h14M22 20h14M22 26h10"/><circle cx="13" cy="33" r="7"/><path d="M8 38l-5 6"/></svg>
    <h3>Discovery.</h3><p>We are passionate about creating with you, not just for you.</p>
    <span class="more" style="top:262px">Learn more →</span>
  </div>
  <div class="card boxed" style="left:464px;top:703px;height:303px">
    <svg class="icon" width="50" height="50" viewBox="0 0 50 50" style="margin-top:55px" fill="none" stroke="#2f8fd8" stroke-width="1.5"><path d="M14 44h24M17 40h18l-2-10c4-4 6-10 3-16-3-6-10-8-15-6l-4 6-5 4 3 4 6-2-3 10z"/></svg>
    <h3>Strategy.</h3><p>Content is only as good as your plan to deliver it.</p>
    <span class="more" style="top:262px">Learn more →</span>
  </div>
  <div class="card" style="left:768px;top:703px;height:303px">
    <svg class="icon" width="50" height="50" viewBox="0 0 50 50" style="margin-top:55px" fill="none" stroke="#2f8fd8" stroke-width="1.5"><path d="M25 8v10M18 18h14l-3 14h-8zM21 32l4 12 4-12"/><circle cx="8" cy="8" r="3"/><circle cx="42" cy="8" r="3"/><path d="M11 8h11M28 8h11"/></svg>
    <h3>Creative.</h3><p>We are ready for our close up! Are you?</p>
    <span class="more" style="top:262px">Learn more →</span>
  </div>
</section>

<section class="abs band" role="img" aria-label="Blue faceted background">
  <h2>Let's talk about what we can build together</h2>
  <p>There are many variations of passages of Lorem Ipsum available but the majority have suffered</p>
  <span class="btn ghost" style="left:416px;top:146px;width:176px;height:39px">Contact Us Today!</span>
  <span class="btn ghost" style="left:608px;top:146px;width:175px;height:39px">Get in Touch</span>
</section>

<section>
  <h2 class="abs about-title">Brightfold Systems</h2>
  <p class="abs about-lead">Lorem Ipsum is simply dummy text of the printing and typesetting industry. Lorem Ipsum has been the industry's standard dummy text ever since the make a type.</p>
  <p class="abs about-body">There are many variations of passages of Lorem Ipsum available, but the majority have suffered alteration in some form, by injected humour, or randomised words which don't look even slightly believable. If you are going to use a passage of Lorem Ipsum, you need to be sure there isn't anything embarrassing hidden in the middle of text.</p>
  <span class="btn" style="left:80px;top:1752px;width:128px;height:39px">About Us</span>
  <div class="abs blob-bg"></div>
  <div class="abs blob-photo" role="img" aria-label="Photo of three colleagues reviewing work at a desk"></div>
</section>

<section>
  <h2 class="sec-title" style="top:1960px">Service we provide</h2>
  <span class="arrow" style="left:108px;top:2160px">←</span>
  <span class="arrow" style="left:1068px;top:2160px">→</span>
  <div class="card" style="left:160px;top:2031px;height:290px">
    <svg class="icon" width="50" height="50" viewBox="0 0 50 50" style="margin-top:45px" fill="none" stroke="#2f8fd8" stroke-width="1.5"><rect x="5" y="6" width="40" height="30" rx="2"/><path d="M5 12h40M10 17h12v12H10zM27 17h13M27 22h13M27 27h9M18 44h14M25 36v8"/></svg>
    <h3>Web development</h3><p>Lorem ipsum dolor amet, consectetur adipiscing elit, sed do eiusmod tempor ...</p>
    <span class="more" style="top:250px">Learn more →</span>
  </div>
  <div class="card boxed" style="left:464px;top:2031px;height:290px">
    <svg class="icon" width="50" height="50" viewBox="0 0 50 50" style="margin-top:45px" fill="none" stroke="#2f8fd8" stroke-width="1.5"><rect x="24" y="5" width="20" height="14" rx="2"/><path d="M32 9l5 3-5 3z"/><path d="M8 24h8l12-8v24l-12-8H8z"/><path d="M10 32l3 12h5"/></svg>
    <h3>Digital marketing</h3><p>Lorem ipsum dolor amet, consectetur adipiscing elit, sed do eiusmod tempor ...</p>
    <span class="more" style="top:250px">Learn more →</span>
  </div>
  <div class="card" style="left:768px;top:2031px;height:290px">
    <svg class="icon" width="50" height="50" viewBox="0 0 50 50" style="margin-top:45px" fill="none" stroke="#2f8fd8" stroke-width="1.5"><rect x="5" y="6" width="40" height="32" rx="2"/><path d="M5 12h40"/><circle cx="25" cy="25" r="7"/><path d="M20 44h10"/></svg>
    <h3>Custom software</h3><p>Lorem ipsum dolor amet, consectetur adipiscing elit, sed do eiusmod tempor ...</p>
    <span class="more" style="top:250px">Learn more →</span>
  </div>
  <span class="btn" style="left:544px;top:2363px;width:112px;height:38px">View All</span>
</section>

<section class="abs work">
  <h2 class="sec-title" style="top:48px">Explore our work</h2>
  <div class="shot" style="left:0;width:128px;background:linear-gradient(160deg,#f6c21f,#1f2a44 60%)" role="img" aria-label="Previous project preview"></div>
  <div class="shot" style="left:161px;width:880px;background:linear-gradient(120deg,#1f7f9a,#2aa3c6 60%,#4cc9ef)" role="img" aria-label="Screenshot of a big data management dashboard shown on a monitor">
    <div class="abs" style="left:216px;top:114px;width:448px;height:245px;background:#0f3f58;border:12px solid #3ab6dc;border-bottom:none"></div>
    <div class="shot-caption"><b>Big data management system frontend</b><span>Web application</span></div>
  </div>
  <div class="shot" style="left:1072px;width:128px;background:linear-gradient(200deg,#1c2740,#243350)" role="img" aria-label="Next project preview"></div>
  <span class="pdot" style="left:543px;background:var(--blue)"></span>
  <span class="pdot" style="left:557px"></span><span class="pdot" style="left:571px"></span>
  <span class="pdot" style="left:585px"></span><span class="pdot" style="left:599px"></span>
  <span class="pdot" style="left:613px"></span><span class="pdot" style="left:627px"></span>
  <span class="pdot" style="left:641px"></span>
</section>

<section>
  <h2 class="sec-title" style="top:3136px">What our clients say</h2>
  <span class="arrow" style="left:108px;top:3255px">←</span>
  <span class="arrow" style="left:1068px;top:3255px">→</span>
  <div class="avatar" style="left:159px;top:3204px" role="img" aria-label="Portrait of client Mara Lindqvist"></div>
  <p class="quote" style="left:311px;top:3212px">There are many variations of passages of Lorem Ipsum available, but the majority have suffered alteration in some form, by injected humour, or randomised words which don't look even slightly believable.</p>
  <p class="person" style="left:311px;top:3372px">Mara Lindqvist,<small>Harbor Studio</small></p>
  <div class="avatar" style="left:631px;top:3204px" role="img" aria-label="Portrait of client Theo Brannan"></div>
  <p class="quote" style="left:783px;top:3212px">There are many variations of passages of Lorem Ipsum available, but the majority have suffered alteration in some form, by injected humour, or randomised words which don't look even slightly believable.</p>
  <p class="person" style="left:783px;top:3372px">Theo Brannan<small>Northline Co.</small></p>
</section>

<section>
  <div class="abs" style="left:80px;top:3531px;width:470px;height:1px;background:#e0e4e8"></div>
  <div class="abs" style="left:650px;top:3531px;width:470px;height:1px;background:#e0e4e8"></div>
  <h3 class="abs" style="left:0;width:1200px;top:3518px;text-align:center;font-size:18px;font-weight:500">Clients</h3>
  <span class="client-logo" style="left:161px">Kestrel</span>
  <span class="client-logo" style="left:340px">Oakmere</span>
  <span class="client-logo" style="left:520px">Vantor</span>
  <span class="client-logo" style="left:699px">Oakmere</span>
  <span class="client-logo" style="left:877px">Kestrel</span>
</section>

<section>
  <div class="abs contact-bg" role="img" aria-label="Soft sky with clouds and distant mountains"></div>
  <h2 class="abs" style="left:0;width:1200px;top:3770px;text-align:center;font-size:28px;font-weight:500;line-height:35px">
    <span style="display:inline-block;width:80px;height:1px;background:#9cc8ea;vertical-align:middle;margin-right:24px"></span>Brightfold Systems, let's start<span style="display:inline-block;width:80px;height:1px;background:#9cc8ea;vertical-align:middle;margin-left:24px"></span><br>something!</h2>
  <div class="field" style="left:241px;top:3863px;width:349px;height:38px">Enter your name*</div>
  <div class="field" style="left:608px;top:3863px;width:351px;height:38px;justify-content:space-between">Project Type*<span style="color:#aaa">⌄</span></div>
  <div class="field" style="left:241px;top:3919px;width:349px;height:38px">E-mail*</div>
  <div class="field area" style="left:608px;top:3919px;width:351px;height:94px">Message ...</div>
  <div class="field" style="left:241px;top:3975px;width:349px;height:38px">Phone</div>
  <span class="btn" style="left:552px;top:4040px;width:95px;height:37px">Send</span>
</section>

<footer class="abs footer">
  <span class="abs" style="left:80px;top:25px">© 2019 Brightfold Systems. All Right Reserved</span>
  <span class="abs" style="left:411px;top:25px">Ph. 555.014.2291</span>
  <span class="abs" style="left:565px;top:25px">E. hello@brightfoldsystems.com</span>
  <span class="social" style="left:969px"></span>
  <span class="social" style="left:1009px"></span>
  <span class="social" style="left:1048px"></span>
  <span class="social" style="left:1089px"></span>
</footer>

</body>
</html>
```